Beef cattle farm needs signs which can be seen from roadside

We would like submissions of artwork for a sign that will hang from a fence or gate and will be seen by passing cars.

Existing logo and branding theme for the company is attached.

Signage can be between 900mm x 400mm - 1200mm x 600mm

Industry/Entity Type

Farm

Requirements
Must have
• the Signs should have the following information:
• Company name: Brindle Ridge Grazing Company
• Address: 214 Wattlebank Hollow Road
• Contact number: 0431 862 475
• email address: admin@brindleridgegrazingco.com.au
• - Logo and branding as per attached artwork

```html
<!DOCTYPE html>
<html lang="en">
<head>
<meta charset="utf-8">
<title>Brindle Ridge Grazing Company – Roadside Sign</title>
<link rel="stylesheet" href="https://fonts.googleapis.com/css2?family=Montserrat:wght@600&family=Open+Sans:wght@300&display=swap">
<style>
  :root {
    --farm-green: #145a36;
    --grass-light: #2f7a52;
    --paper: #ffffff;
  }
  html, body {
    margin: 0;
    padding: 0;
    width: 1200px;
    height: 619px;
    overflow: hidden;
    background: var(--paper);
  }
  .sign {
    position: relative;
    width: 1200px;
    height: 619px;
    background: var(--paper);
  }
  .sign-art {
    position: absolute;
    inset: 0;
    display: block;
  }
  .brand-name {
    font-family: "Montserrat", Arial, sans-serif;
    font-weight: 600;
    fill: var(--farm-green);
  }
  .contact-list {
    position: absolute;
    left: 0;
    top: 0;
    margin: 0;
    padding: 0;
    list-style: none;
    font-family: "Open Sans", Arial, sans-serif;
    font-weight: 300;
    color: var(--paper);
  }
  .contact-item {
    position: absolute;
    left: 562px;
    white-space: nowrap;
    line-height: 1;
  }
  .contact-email { top: 143px; font-size: 33px; }
  .contact-address { top: 226px; font-size: 41px; }
  .contact-phone { top: 314px; font-size: 41px; }
</style>
</head>
<body>
<main class="sign">
  <svg class="sign-art" width="1200" height="619" viewBox="0 0 1200 619" aria-hidden="false">
    <defs>
      <clipPath id="panel-shape">
        <path d="M357 77 H1179 V608 H424 C455 450 475 250 357 77 Z"/>
      </clipPath>
      <linearGradient id="grass-tone" x1="0" y1="0" x2="0" y2="1">
        <stop offset="0" stop-color="#145a36"/>
        <stop offset="0.55" stop-color="#5e9a78"/>
        <stop offset="1" stop-color="#cfe2d6"/>
      </linearGradient>
    </defs>

    <!-- contact panel -->
    <path class="contact-panel" d="M357 77 H1179 V608 H424 C455 450 475 250 357 77 Z" fill="var(--farm-green)"/>
    <rect class="grass-band" x="357" y="370" width="822" height="238" fill="url(#grass-tone)"
          clip-path="url(#panel-shape)" role="img" aria-label="White grass blades rising along the bottom of the panel"/>

    <!-- brand block, left -->
    <circle class="brand-disc" cx="212" cy="216" r="144" fill="var(--farm-green)"/>
    <text class="brand-name" x="4" y="446" font-size="62" textLength="412" lengthAdjust="spacingAndGlyphs">BRINDLE RIDGE</text>
    <text class="brand-name" x="4" y="494" font-size="32" textLength="412" lengthAdjust="spacingAndGlyphs">GRAZING COMPANY</text>

    <!-- brand block, top right -->
    <text class="brand-name" x="1152" y="37" font-size="40" text-anchor="end" textLength="226" lengthAdjust="spacingAndGlyphs">BRINDLE RIDGE</text>
    <text class="brand-name" x="1152" y="63" font-size="17" text-anchor="end" textLength="226" lengthAdjust="spacingAndGlyphs">GRAZING COMPANY</text>

    <!-- contact icons -->
    <g class="icon icon-email" fill="none" stroke="var(--paper)" stroke-width="3">
      <circle cx="512" cy="162" r="24"/>
      <rect x="499" y="153" width="26" height="18" fill="var(--paper)" stroke="none"/>
      <path d="M499 154 L512 164 L525 154" stroke="var(--farm-green)" stroke-width="2"/>
    </g>
    <g class="icon icon-pin" fill="none" stroke="var(--paper)" stroke-width="3">
      <circle cx="512" cy="249" r="24"/>
      <path d="M512 264 C504 254 502 249 502 244 A10 10 0 0 1 522 244 C522 249 520 254 512 264 Z" stroke-width="2.5"/>
      <circle cx="512" cy="244" r="3.5" fill="var(--paper)" stroke="none"/>
    </g>
    <g class="icon icon-phone" fill="none" stroke="var(--paper)" stroke-width="3">
      <circle cx="512" cy="337" r="24"/>
      <path d="M504 326 L509 324 L512 331 L509 334 C511 339 513 341 517 343 L520 340 L527 343 L525 348 C513 349 502 338 504 326 Z" stroke-width="2.2" stroke-linejoin="round"/>
    </g>
  </svg>

  <ul class="contact-list">
    <li class="contact-item contact-email">admin@brindleridgegrazingco.com.au</li>
    <li class="contact-item contact-address">214 Wattlebank Hollow Road</li>
    <li class="contact-item contact-phone">0431 862 475</li>
  </ul>
</main>
</body>
</html>
```